an A3 Folded in half to A4 brochure for strata management company

Color scheme must match logo and website. Must have pictures that deliver the meaning of the wording part. Please refer to the flyer artwork enclosed. Contents are provided as enclosed.

Target Market(s)

Developers or strata title property owners

Industry/Entity Type

It Company

Font styles to use
Serif

Requirements
Must have
• 1) professional layout, simple and easy to read
• 2) Have relevant pictures such as building and people to deliver the meaning of the wording part. Please refer to the flier artwork enclosed.
• I.e. Service for developer, has people's picture of developer looking.
• 3) The brochure should work as a 24/7 marketer to promote the business rather than a nice picture and cannot get viewers to pick up the phone.
• 4) please make the color theme warm
• 5) should have clear call for action
Should not have
• Please do not make it too colorful which will distract people.

```html
<!DOCTYPE html>
<html lang="en">
<head>
<meta charset="utf-8">
<title>Northgate Strata Management – Brochure Cover</title>
<link href="https://fonts.googleapis.com/css2?family=Open+Sans:wght@400;600;700&display=swap" rel="stylesheet">
<style>
  :root {
    --backdrop: #d9d9d9;
    --paper: #ffffff;
    --paper-shade: #f1f1f1;
    --brand-red: #dc2626;
    --brand-yellow: #e8aa3c;
    --sky-top: #6f8fc4;
    --sky-low: #b9c9e0;
    --building: #c9803d;
    --ink: #3a3a3a;
    --footer-grey: #5f6062;
    --badge-blue: #2b8fd0;
  }
  * { box-sizing: border-box; margin: 0; padding: 0; }
  html, body { width: 1200px; height: 900px; overflow: hidden; }
  body {
    background: var(--backdrop);
    font-family: "Open Sans", Arial, sans-serif;
    display: flex; align-items: center; justify-content: center;
  }
  .cover {
    position: relative;
    width: 608px; height: 860px;
    background: linear-gradient(180deg, var(--paper) 0%, var(--paper-shade) 100%);
    box-shadow: 0 10px 30px rgba(0,0,0,.18);
    overflow: hidden;
  }
  .cover__art { position: absolute; inset: 0; }
  .brand {
    position: absolute; left: 40px; top: 64px;
    display: flex; align-items: center; gap: 12px;
  }
  .brand__dot {
    width: 54px; height: 54px; border-radius: 50%;
    background: var(--brand-red);
  }
  .brand__name {
    font-size: 30px; font-weight: 700; color: var(--brand-red); line-height: 1;
  }
  .brand__tag {
    font-size: 13px; font-weight: 700; color: var(--ink); margin-top: 4px;
  }
  .headline {
    position: absolute; left: 40px; top: 588px;
    color: #fff; font-size: 24px; font-weight: 400; line-height: 1.3;
    white-space: nowrap;
  }
  .offer {
    position: absolute; left: 40px; top: 742px; width: 330px;
  }
  .offer__intro {
    font-size: 12px; color: var(--ink); line-height: 1.4; margin-bottom: 6px;
  }
  .offer__list { list-style: none; }
  .offer__item {
    display: flex; align-items: center; gap: 8px;
    background: var(--brand-red); color: #fff;
    font-size: 11.5px; height: 22px; padding: 0 10px;
    margin-bottom: 4px;
  }
  .offer__item:nth-child(2) { margin-left: 8px; }
  .offer__item svg { flex: none; }
  .membership {
    position: absolute; right: 36px; top: 712px; width: 150px;
  }
  .membership__note { font-size: 8px; color: var(--ink); margin-bottom: 5px; }
  .membership__badge {
    width: 110px; height: 30px; border-radius: 4px; background: var(--badge-blue);
  }
</style>
</head>
<body>
  <main class="cover">
    <svg class="cover__art" width="608" height="860" viewBox="0 0 608 860">
      <defs>
        <linearGradient id="photoTone" x1="0" y1="0" x2="0" y2="1">
          <stop offset="0" stop-color="#6f8fc4"/>
          <stop offset=".45" stop-color="#b9c9e0"/>
          <stop offset=".55" stop-color="#c9803d"/>
          <stop offset="1" stop-color="#8a5a30"/>
        </linearGradient>
      </defs>
      <polygon class="accent-strip" points="296,152 608,152 608,160 288,160" fill="#dc2626"/>
      <polygon class="hero-photo" role="img"
        aria-label="Photo: smiling couple holding new keys in front of a modern apartment building"
        points="0,200 270,200 300,160 608,160 608,480 0,570" fill="url(#photoTone)"/>
      <polygon class="headline-band" points="0,560 608,470 608,650 0,730" fill="#e8aa3c"/>
      <rect class="footer-bar" x="0" y="832" width="608" height="28" fill="#5f6062"/>
    </svg>

    <div class="brand">
      <span class="brand__dot"></span>
      <div>
        <div class="brand__name">Northgate</div>
        <div class="brand__tag">Strata Management</div>
      </div>
    </div>

    <h1 class="headline">At Northgate strata we treat your<br>property like we would our own!</h1>

    <section class="offer">
      <p class="offer__intro">We offer tailor made strata management service to owners/developers of:</p>
      <ul class="offer__list">
        <li class="offer__item">
          <svg width="10" height="10" viewBox="0 0 10 10"><path d="M1 5.5 4 8.5 9 1.5" fill="none" stroke="#fff" stroke-width="1.6"/></svg>
          Residential/Mixed use properties
        </li>
        <li class="offer__item">
          <svg width="10" height="10" viewBox="0 0 10 10"><path d="M1 5.5 4 8.5 9 1.5" fill="none" stroke="#fff" stroke-width="1.6"/></svg>
          Commercial/Industrial properties
        </li>
      </ul>
    </section>

    <aside class="membership">
      <p class="membership__note">Northgate is proud a member of</p>
      <div class="membership__badge" role="img" aria-label="Industry association membership badge"></div>
    </aside>
  </main>
</body>
</html>
```